Website for an interior designer

We need a new website for Clara Beth Holloway whose new business name is Clara Beth Holloway Interiors. She is a residential interior designer with a mix of modern and contemporary tastes. We are in the process of overhauling her website which is +15 years old and not an accurate reflection of her tastes. The uploaded photos are from some of the houses she has done as well as her logo(s). We would need a section for "About Us" that would have a paragraph of text and bullets showing services and a gallery for photos (~12 total, more to come). A contract page would be optional. The client likes the feel/look of this website: https://www.pondrickstudio.example/ but doesn't want to copy it exactly.

Target Market(s)

Upscale home owners

Industry/Entity Type

Interior Design

Coding

Coded - Design and coding required

Number of Pages Required

4 page

Colors

Designer to choose only greyscale colors for use in the design.

Requirements
Must have
• Home page, about us page, gallery page, contact us page.

```html
<!DOCTYPE html>
<html lang="en">
<head>
<meta charset="utf-8">
<title>Clara Beth Holloway Interiors</title>
<link rel="stylesheet" href="https://fonts.googleapis.com/css2?family=Playfair+Display:wght@400&family=Roboto:wght@300;400;500;700&display=swap">
<style>
:root{
  --white:#ffffff;
  --ink:#333333;
  --text:#555555;
  --muted:#8c8c8c;
  --nav:#6e6e6e;
  --light-band:#e8e8e8;
  --mid-band:#8a8a8a;
  --dark-band:#333333;
  --line:#9a9a9a;
  --serif:'Playfair Display', Georgia, serif;
  --sans:'Roboto', Arial, sans-serif;
}
*{box-sizing:border-box;margin:0;padding:0}
html,body{width:1200px;height:3548px;overflow:hidden}
body{position:relative;background:var(--white);font-family:var(--sans);color:var(--text)}
.abs{position:absolute}

/* header */
.site-header{position:absolute;left:0;top:0;width:1200px;height:138px;background:var(--white)}
.brand{position:absolute;left:0;width:1200px;top:56px;text-align:center;font-family:var(--serif);font-size:20px;letter-spacing:2px;color:var(--ink);text-transform:uppercase;line-height:1.4}
.brand small{display:block;font-size:11px;letter-spacing:6px}
.header-phone{position:absolute;right:60px;top:86px;font-size:22px;color:var(--text);display:flex;align-items:center;gap:8px}

.main-nav{position:absolute;left:0;top:138px;width:1200px;height:65px;background:var(--nav);display:flex;justify-content:center;align-items:center}
.main-nav a{color:var(--white);text-decoration:none;font-size:16px;padding:0 37px;border-left:1px solid #a5a5a5;line-height:20px}
.main-nav a:first-child{border-left:none;font-weight:700}

/* hero */
.hero{position:absolute;left:0;top:203px;width:1200px;height:593px;background:linear-gradient(100deg,#e9e7e3 0%,#d9d4cc 35%,#bfb5a8 60%,#8c7a68 100%)}
.hero-arrow{position:absolute;top:270px}
.hero-card{position:absolute;left:609px;top:123px;width:495px;height:304px;background:rgba(75,75,75,.92);text-align:center;color:var(--white)}
.hero-card .name{margin-top:88px;font-family:var(--serif);font-size:36px;text-transform:uppercase}
.hero-card .sub{font-family:var(--serif);font-size:28px;letter-spacing:5px;margin-top:2px}
.btn{display:inline-block;border:2px solid currentColor;border-radius:30px;text-decoration:none;text-transform:uppercase;font-size:17px;text-align:center}
.hero-card .btn{margin-top:14px;width:164px;height:46px;line-height:42px;color:var(--white);font-size:16px}

/* sections */
.eyebrow{font-size:17px;letter-spacing:3px;text-transform:uppercase;color:var(--muted);font-weight:300}
.section-title{font-family:var(--serif);font-size:42px;text-transform:uppercase;color:var(--ink);font-weight:400;line-height:1.15}
.rule{width:44px;height:2px;background:var(--line)}

.about{position:absolute;left:0;top:796px;width:1200px;height:452px;text-align:center}
.about .eyebrow{position:absolute;left:0;width:1200px;top:86px}
.about .section-title{position:absolute;left:0;width:1200px;top:115px}
.about .rule{position:absolute;left:578px;top:174px}
.about p{position:absolute;left:120px;width:960px;top:208px;font-size:16.5px;line-height:31px;color:var(--text)}
.about .btn{position:absolute;left:515px;top:325px;width:188px;height:53px;line-height:49px;color:var(--text)}

.services{position:absolute;left:0;top:1248px;width:1200px;height:538px;background:var(--light-band)}
.services-photo{position:absolute;left:110px;top:83px;width:500px;height:347px;background:linear-gradient(160deg,#e6e4df,#b9b5ad 55%,#6f665c)}
.services .eyebrow{position:absolute;left:660px;top:83px}
.services .section-title{position:absolute;left:658px;top:110px}
.services .rule{position:absolute;left:666px;top:154px;width:34px}
.service-list{position:absolute;left:660px;top:180px;list-style:none}
.service-list li{display:flex;align-items:center;height:41.7px;font-size:16px;color:var(--ink)}
.service-list svg{margin-right:16px}

.gallery{position:absolute;left:0;top:1786px;width:1200px;height:949px;background:var(--mid-band);text-align:center}
.gallery .eyebrow{position:absolute;left:0;width:1200px;top:68px;color:#e6e6e6}
.gallery .section-title{position:absolute;left:0;width:1200px;top:94px;color:var(--white)}
.gallery .rule{position:absolute;left:590px;top:146px;background:#c8c8c8}
.gallery-grid{position:absolute;left:84px;top:199px;width:1061px;display:grid;grid-template-columns:repeat(4,1fr);gap:4px}
.gallery-grid div{height:197px}
.gallery .btn{position:absolute;left:507px;top:836px;width:180px;height:58px;line-height:54px;color:var(--white)}

.contact{position:absolute;left:0;top:2735px;width:1200px;height:656px;background:var(--dark-band);color:var(--white)}
.contact .eyebrow{position:absolute;left:0;width:1200px;text-align:center;top:60px;color:#d0d0d0}
.contact .section-title{position:absolute;left:0;width:1200px;text-align:center;top:85px;color:var(--white)}
.contact .rule{position:absolute;left:589px;top:137px;background:#bbbbbb}
.contact-item{position:absolute;top:176px;display:flex;align-items:center;gap:12px}
.contact-item .icon{width:60px;height:60px;border-radius:50%;background:#6f6f6f;display:flex;align-items:center;justify-content:center}
.contact-item .label{font-size:14px;color:#cfcfcf;text-transform:uppercase}
.contact-item .value{font-size:16px;color:var(--white);margin-top:4px}
.contact-item .value.big{font-size:22px;font-weight:700}
.field{position:absolute;border:2px solid #9a9a9a;font-size:15px;color:#d9d9d9;padding:0 26px;display:flex;align-items:center}
.field.area{align-items:flex-start;padding-top:16px}
.contact .btn{position:absolute;left:521px;top:542px;width:172px;height:56px;line-height:52px;color:var(--white);font-size:19px;font-weight:500}

.site-footer{position:absolute;left:0;top:3391px;width:1200px;height:157px;background:var(--white)}
.footer-brand{position:absolute;left:120px;top:48px;width:120px;font-family:var(--serif);font-size:17px;line-height:1.2;color:var(--ink);text-align:center}
.footer-nav{position:absolute;left:317px;top:53px;display:flex;gap:58px}
.footer-nav a{font-size:16px;color:var(--ink);text-decoration:none}
.copyright{position:absolute;left:317px;top:90px;font-size:14px;color:var(--muted)}
.social{position:absolute;left:972px;top:43px;display:flex;gap:6px}
.social span{width:40px;height:40px;border:2px solid var(--ink);border-radius:50%}
</style>
</head>
<body>

<header class="site-header">
  <div class="brand">Clara Beth Holloway<small>Interiors</small></div>
  <div class="header-phone">
    <svg width="20" height="20" viewBox="0 0 24 24" fill="none" stroke="#555" stroke-width="2"><path d="M5 3h4l2 5-3 2a12 12 0 0 0 6 6l2-3 5 2v4a2 2 0 0 1-2 2A18 18 0 0 1 3 5a2 2 0 0 1 2-2z"/></svg>
    (555) 018 2240
  </div>
</header>

<nav class="main-nav">
  <a href="#">HOME</a><a href="#">ABOUT US</a><a href="#">SERVICES</a><a href="#">GALLERY</a><a href="#">CONTACT</a>
</nav>

<section class="hero" role="img" aria-label="Bright white kitchen with island, wooden bar stools and pendant lights">
  <svg class="hero-arrow" style="left:32px" width="22" height="40" viewBox="0 0 22 40"><path d="M20 2L3 20l17 18" fill="none" stroke="#222" stroke-width="2.5"/></svg>
  <svg class="hero-arrow" style="left:1150px" width="22" height="40" viewBox="0 0 22 40"><path d="M2 2l17 18L2 38" fill="none" stroke="#222" stroke-width="2.5"/></svg>
  <div class="hero-card">
    <div class="name">Clara Beth Holloway</div>
    <div class="sub">INTERIOR</div>
    <a class="btn" href="#">Contact Us</a>
  </div>
</section>

<section class="about">
  <div class="eyebrow">Overview</div>
  <h2 class="section-title">About Clara Beth Holloway</h2>
  <div class="rule"></div>
  <p>Clara Beth Holloway has extensive experience in all aspects of interior design. She has worked on a wide array of residential and commercial projects in her hometown of Alder Creek and across the United States. Clara Beth's taste can best be described as a sophisticated blend of modern and traditional styles that combine to create a clean, timeless space.</p>
  <a class="btn" href="#">Read More</a>
</section>

<section class="services">
  <div class="services-photo" role="img" aria-label="Light living room with tall black-framed windows and white sofas"></div>
  <div class="eyebrow">What We Do</div>
  <h2 class="section-title">Our Services</h2>
  <div class="rule"></div>
  <ul class="service-list">
    <li><svg width="10" height="16" viewBox="0 0 10 16"><path d="M2 2l6 6-6 6" fill="none" stroke="#333" stroke-width="2"/></svg>Concept Origination and Project Management</li>
    <li><svg width="10" height="16" viewBox="0 0 10 16"><path d="M2 2l6 6-6 6" fill="none" stroke="#333" stroke-width="2"/></svg>Review of Proposed Plans for New Construction and Remodels</li>
    <li><svg width="10" height="16" viewBox="0 0 10 16"><path d="M2 2l6 6-6 6" fill="none" stroke="#333" stroke-width="2"/></svg>Procurement of Furniture, Accents, Art, Fixtures and Fittings</li>
    <li><svg width="10" height="16" viewBox="0 0 10 16"><path d="M2 2l6 6-6 6" fill="none" stroke="#333" stroke-width="2"/></svg>Selection of Paints, Finishes and Construction Materials</li>
    <li><svg width="10" height="16" viewBox="0 0 10 16"><path d="M2 2l6 6-6 6" fill="none" stroke="#333" stroke-width="2"/></svg>Vendor Coordination and Recommendations</li>
    <li><svg width="10" height="16" viewBox="0 0 10 16"><path d="M2 2l6 6-6 6" fill="none" stroke="#333" stroke-width="2"/></svg>Home Staging, Styling and Editing</li>
  </ul>
</section>

<section class="gallery">
  <div class="eyebrow">Our Work</div>
  <h2 class="section-title">Gallery</h2>
  <div class="rule"></div>
  <div class="gallery-grid">
    <div role="img" aria-label="Brick patio with black awning and outdoor seating" style="background:linear-gradient(160deg,#6b4a3e,#3a302b 60%,#a89c8a)"></div>
    <div role="img" aria-label="Covered outdoor living room with sofas" style="background:linear-gradient(160deg,#e8e6e2,#9a7f70 60%,#6a5a50)"></div>
    <div role="img" aria-label="White dining table with white chairs" style="background:linear-gradient(160deg,#f2f1ef,#dcdad6 60%,#6c6660)"></div>
    <div role="img" aria-label="White spiral staircase with dark treads" style="background:linear-gradient(160deg,#f4f4f2,#d8d8d4 60%,#8a8a86)"></div>
    <div role="img" aria-label="Bright living room with grey sofa" style="background:linear-gradient(160deg,#f3f1ec,#cfc8bd 60%,#b08a66)"></div>
    <div role="img" aria-label="Round glass table with cream chairs" style="background:linear-gradient(160deg,#ece7e0,#d6cdc2 60%,#9c9186)"></div>
    <div role="img" aria-label="Library sitting room with fireplace and bookshelves" style="background:linear-gradient(160deg,#5e6770,#3f454b 60%,#8b8f90)"></div>
    <div role="img" aria-label="Dining room with gilded mirror and chandelier" style="background:linear-gradient(160deg,#c9a872,#e6dac6 55%,#8a6c4a)"></div>
    <div role="img" aria-label="Cosy living room with striped pillows and wicker chest" style="background:linear-gradient(160deg,#ded6c8,#f0ebe2 55%,#9a7a56)"></div>
    <div role="img" aria-label="Hallway with bright multicoloured bench" style="background:linear-gradient(160deg,#e6d36a,#d46a9a 55%,#5a4a6a)"></div>
    <div role="img" aria-label="Dining room with framed art and wooden table" style="background:linear-gradient(160deg,#d8d2c6,#8c6a48 60%,#3e3630)"></div>
    <div role="img" aria-label="Open staircase and kitchen with wood accents" style="background:linear-gradient(160deg,#f2f0ec,#d6c5a8 55%,#7a6a58)"></div>
  </div>
  <a class="btn" href="#">View All</a>
</section>

<section class="contact">
  <div class="eyebrow">Get In Touch</div>
  <h2 class="section-title">Contact Us</h2>
  <div class="rule"></div>

  <div class="contact-item" style="left:168px">
    <div class="icon"><svg width="26" height="26" viewBox="0 0 24 24" fill="none" stroke="#fff" stroke-width="1.5"><path d="M5 3h4l2 5-3 2a12 12 0 0 0 6 6l2-3 5 2v4a2 2 0 0 1-2 2A18 18 0 0 1 3 5a2 2 0 0 1 2-2z"/></svg></div>
    <div><div class="label">Phone</div><div class="value big">555 014 7721</div></div>
  </div>
  <div class="contact-item" style="left:467px">
    <div class="icon"><svg width="26" height="26" viewBox="0 0 24 24" fill="none" stroke="#fff" stroke-width="1.5"><path d="M12 22s7-7 7-12a7 7 0 0 0-14 0c0 5 7 12 7 12z"/><circle cx="12" cy="10" r="2.5"/></svg></div>
    <div><div class="label">Address</div><div class="value">Alder Creek Ohio</div></div>
  </div>
  <div class="contact-item" style="left:795px">
    <div class="icon"><svg width="24" height="24" viewBox="0 0 24 24" fill="none" stroke="#fff" stroke-width="1.5"><rect x="3" y="6" width="18" height="13"/><path d="M3 6l9 7 9-7"/></svg></div>
    <div><div class="label">Email Address</div><div class="value">hello@hollowayhome.example</div></div>
  </div>

  <div class="field" style="left:190px;top:285px;width:404px;height:50px">First Name*</div>
  <div class="field" style="left:608px;top:285px;width:404px;height:50px">Last Name*</div>
  <div class="field" style="left:190px;top:350px;width:404px;height:50px">Email address*</div>
  <div class="field" style="left:608px;top:350px;width:404px;height:50px">Phone*</div>
  <div class="field area" style="left:190px;top:414px;width:822px;height:111px">Message</div>
  <a class="btn" href="#">Submit</a>
</section>

<footer class="site-footer">
  <div class="footer-brand">Clara Beth Holloway</div>
  <nav class="footer-nav">
    <a href="#">HOME</a><a href="#">ABOUT US</a><a href="#">SERVICES</a><a href="#">GALLERY</a><a href="#">CONTACT</a>
  </nav>
  <div class="copyright">© 2020 Clarabeth Holloway | All Rights Reserved</div>
  <div class="social" aria-label="Social links"><span></span><span></span><span></span></div>
</footer>

</body>
</html>
```